Become an EMT and Serve your community!

We are looking to design a postcard that will be mailed to surrounding communities that notifies them of our upcoming EMT class with an emphasis of serving their community. We are looking for a design that grabs peoples attention and motivates them to sign up and serve their community. Our primary colors are red and blue. We would like to incorporate the Institute logo as well as one or two photos. We do have more photos available upon request. Our Institute website is www.halvorsenacademy.net for more material. It is important that the postcard meets mailing guidelines.

Target Market(s)

Local community members

Industry/Entity Type

Education

Font styles to use
Sans Serif

Colors
f04a50
3176b5
0255a3
eaf1f7

Requirements
Must have
• Dates
Prices
Contact info
Look interesting
Convey the message of “Serving your Community”
Nice to have
• Clear information
Concise
Incorporate an action shot
Should not have
• Generic EMS logos

```html
<!DOCTYPE html>
<html lang="en">
<head>
<meta charset="utf-8">
<title>2020 Summer EMT Class Postcard</title>
<link href="https://fonts.googleapis.com/css2?family=Montserrat:wght@400;500;600;700;800&family=Oswald:wght@600&display=swap" rel="stylesheet">
<style>
  :root{
    --purple:#2e1a63;
    --grey-text:#606060;
    --ink:#222;
    --panel:#e9e9e9;
    --strip:#ececec;
    --bg:#d8d3cc;
    --white:#fff;
    --photo-a:#8a7f7a;
    --photo-b:#c9372f;
  }
  *{box-sizing:border-box;margin:0;padding:0}
  html,body{width:1200px;height:1200px;overflow:hidden}
  body{background:var(--bg);font-family:'Montserrat',sans-serif;position:relative}
  .card{position:absolute;left:250px;width:700px;background:var(--white);box-shadow:0 6px 18px rgba(0,0,0,.25);overflow:hidden}
  .front{top:60px;height:500px}
  .back{top:600px;height:500px}
  .abs{position:absolute}

  /* front */
  .hero-photo{left:0;top:0;width:700px;height:319px;background:linear-gradient(135deg,#6f6a68 0%,#9b9390 40%,var(--photo-b) 75%,#7c2a25 100%)}
  .year{left:22px;top:332px;font-family:'Oswald',sans-serif;font-weight:600;font-size:90px;line-height:1;color:var(--purple);letter-spacing:-2px;transform:scaleX(.92);transform-origin:left}
  .class-title{left:188px;top:340px;font-weight:800;font-size:40px;line-height:38px;color:var(--grey-text)}
  .tuition{left:453px;top:255px;width:213px;height:182px;background:var(--purple);border-radius:12px;color:var(--white);text-align:center;padding-top:22px}
  .tuition .label{font-weight:600;font-size:24px}
  .tuition .price{font-weight:700;font-size:44px;line-height:48px;margin-top:2px}
  .tuition .price sup{font-size:22px;vertical-align:top;position:relative;top:2px}
  .tuition .price small{font-size:18px;font-weight:700;margin-left:6px}
  .tuition .note{font-size:19px;font-weight:500}
  .tuition .deposit{font-size:13.5px;margin-top:6px;line-height:17px}
  .call-bar{left:0;top:438px}
  .call-text{left:22px;top:454px;color:var(--white);font-weight:800;font-size:25px;letter-spacing:.3px}
  .web-front{right:36px;top:460px;font-size:14.5px;font-weight:500;color:var(--ink)}

  /* back */
  .headline{left:22px;top:18px;font-weight:800;font-size:42px;line-height:40px;color:var(--purple)}
  .when-panel{left:0;top:113px;width:362px;height:125px;background:var(--panel)}
  .when-tab{left:0;top:106px}
  .when-label{left:24px;top:107px;color:var(--white);font-weight:700;font-size:17px}
  .when-col{font-size:9.6px;line-height:11.7px;color:var(--ink)}
  .when-col b{font-weight:700}
  .col-left{left:23px;top:145px;width:176px}
  .col-right{left:216px;top:145px;width:130px;text-align:justify;border-left:1px solid #555;padding-left:10px;height:78px;margin-left:-3px}
  .photo-left{left:0;top:238px;width:178px;height:88px;background:linear-gradient(120deg,#d7b89c,#6b6b70)}
  .photo-right{left:181px;top:238px;width:181px;height:88px;background:linear-gradient(120deg,#1c1d22,#4a5a3a 60%,#2a2a30)}
  .photo-rule{left:0;top:326px;width:362px;height:8px;background:#777}
  .body-copy{left:18px;top:348px;width:330px;font-size:9.8px;line-height:11.7px;text-align:justify;color:var(--ink)}
  .phone-bar{left:0;top:403px}
  .phone-text{left:58px;top:413px;color:var(--white);font-weight:800;font-size:27px}
  .phone-icon{left:28px;top:409px}
  .web-back{left:42px;top:467px;font-size:14px;font-weight:500;color:var(--ink);display:flex;align-items:center;gap:7px}
  .bottom-rule{left:0;top:490px;width:700px;height:10px;background:#666}
  .return{left:383px;top:60px;font-size:8.2px;line-height:10px;color:var(--ink)}
  .return .lbl{color:var(--purple);font-weight:700}
  .return .org{font-weight:700}
  .stamp{left:619px;top:38px;width:50px;height:58px;background:var(--strip)}
  .addr-line{left:383px;width:286px;height:1px;background:#e3e3e3}
  .brand{left:575px;top:430px;display:flex;align-items:center;gap:6px;font-weight:700;font-size:11px;color:var(--photo-b)}
  .brand .mark{width:12px;height:12px;background:var(--photo-b)}
</style>
</head>
<body>

<section class="card front">
  <div class="abs hero-photo" role="img" aria-label="Photo of two EMTs in red jackets inside an ambulance"></div>
  <div class="abs year">2020</div>
  <div class="abs class-title">SUMMER<br>EMT CLASS</div>
  <div class="abs tuition">
    <div class="label">Tuition</div>
    <div class="price"><sup>$</sup>1000<small>EMT</small></div>
    <div class="note">(without CPR)</div>
    <div class="deposit">$250 deposit is due at time<br>of registration.</div>
  </div>
  <svg class="abs call-bar" width="700" height="62" viewBox="0 0 700 62">
    <polygon points="410,0 700,0 700,62 458,62" fill="var(--strip)"/>
    <polygon points="0,0 375,0 431,62 0,62" fill="var(--purple)"/>
  </svg>
  <div class="abs call-text">CALL US 555-014-2290</div>
  <div class="abs web-front">www.halvorsenacademy.net</div>
</section>

<section class="card back">
  <div class="abs headline">SERVING YOUR<br>COMMUNITY</div>
  <div class="abs when-panel"></div>
  <svg class="abs when-tab" width="100" height="24" viewBox="0 0 100 24">
    <polygon points="0,0 100,0 78,24 0,24" fill="var(--purple)"/>
  </svg>
  <div class="abs when-label">When</div>
  <div class="abs when-col col-left">Monday, Tuesday, Wednesday from <b>May 26th through August 17th.</b><br><br><b>Wednesdays:</b><br>Students will need to sign up for either a <b>4:00p-7:00p</b> lab section, or a <b>7:00p-10:0p</b> lab section.</div>
  <div class="abs when-col col-right">There will be one required Sat/Sun weekend held for all students. This will take place on June 13th &amp; 14th. Weekend classes will run from <b>8:00am - 8:00pm.</b></div>
  <div class="abs photo-left" role="img" aria-label="Photo of students practicing CPR on a training manikin"></div>
  <div class="abs photo-right" role="img" aria-label="Action photo of EMTs loading a patient on a stretcher at night"></div>
  <div class="abs photo-rule"></div>
  <p class="abs body-copy">Serve your community and become an Emergency Medical Technician. As a student you will have access to cutting edge training equipment, experienced instructors, and be able to train on a 911 Ambulance through Halvorsen EMS.</p>
  <svg class="abs phone-bar" width="362" height="55" viewBox="0 0 362 55">
    <polygon points="0,0 362,0 315,55 0,55" fill="var(--purple)"/>
  </svg>
  <svg class="abs phone-icon" width="20" height="40" viewBox="0 0 20 40">
    <path d="M8 2 L14 2 L14 10 L10 12 Q7 20 10 28 L14 30 L14 38 L8 38 Q0 20 8 2 Z" fill="var(--white)"/>
  </svg>
  <div class="abs phone-text">555-014-2290</div>
  <div class="abs web-back">
    <svg width="12" height="12" viewBox="0 0 12 12" fill="none" stroke="#222" stroke-width="1.2">
      <circle cx="6" cy="6" r="5"/><ellipse cx="6" cy="6" rx="2.2" ry="5"/><line x1="1" y1="6" x2="11" y2="6"/>
    </svg>
    www.halvorsenacademy.net
  </div>
  <div class="abs bottom-rule"></div>

  <div class="abs return">
    <div class="lbl">Return to:</div>
    <div class="org">Halvorsen Academy of EMS</div>
    <div>18 Alder Lane</div>
    <div>Easton, NH 03580</div>
  </div>
  <div class="abs stamp"></div>
  <div class="abs addr-line" style="top:156px"></div>
  <div class="abs addr-line" style="top:222px"></div>
  <div class="abs addr-line" style="top:289px"></div>
  <div class="abs addr-line" style="top:356px"></div>
  <div class="abs brand"><span class="mark"></span>Halvorsen EMS</div>
</section>

</body>
</html>
```